Bright Path Consultant needs Business Card & Banner

I am a new consultant / compassionate communication trainer who needs to focus on her A-Game... Turning Tension into Understanding!

I am looking for a Business Card and Home Page Banner for my website and possible use on a Facebook Page.

I have a draft of a website (sqarespace) done (can provide the password to view) and have taken a crack at my own business cards. I have an idea what I want and need help completing.

Business name - Willow Dawn
Tag line - Turning Tension into Understanding
Vision (draft) - To cultivate harmonious relationships by building individual and organizational capacity for compassion and collaboration.
Services - I provide individual empathic coaching, interpersonal mediation and for organizations I offer collaborative communication training.

I have provided pics of me and images from my own photo stock.

Banner
I'd like the banner photo to include an image from nature and my image with my business name and tag line.

Business Card
Two sided with one of the heart images on one side and personal details on the other. Example provided.

Of course, the reason I'm hear is I need help so please feel free to improve on my ideas in any way you like.

Target Market(s)

Small to Medium sized corporations
Non-Profits
Individuals

Industry/Entity Type

Consultant

Contact Information for Business Card

Mira Dalton
Consultant (or Founder?)

Interpersonal Mediation
Collaborative Communication
phone 1-604-555-0182
mira@willowdawn.ca
www.willowdawn.ca

Requirements
Must have
• colour
• two sided
• clean lines
• strong & feminine
• canadian spellings
Nice to have
• for example see the attached pdf - WD Business Card design v4

```html
<!DOCTYPE html>
<html lang="en">
<head>
<meta charset="utf-8">
<title>Willow Dawn – Business Card</title>
<link href="https://fonts.googleapis.com/css2?family=Questrial&display=swap" rel="stylesheet">
<style>
  :root {
    --bg: #ece9e4;
    --card: #ffffff;
    --plum: #b533b3;
    --leaf: #8cc63f;
    --leaf-dark: #6fae2a;
    --forest-a: #3f5a2c;
    --forest-b: #6b8a4a;
    --shore-a: #2b3238;
    --shore-b: #a9b4b8;
  }
  * { box-sizing: border-box; margin: 0; padding: 0; }
  html, body { width: 1200px; height: 780px; overflow: hidden; }
  body {
    background: var(--bg);
    font-family: "Questrial", sans-serif;
    position: relative;
  }
  .card {
    position: absolute;
    top: 235px;
    width: 540px;
    height: 309px;
    background: var(--card);
    border-radius: 4px;
    box-shadow: 0 6px 18px rgba(0,0,0,.18);
    overflow: hidden;
  }
  .card--front { left: 40px; }
  .card--back { left: 620px; }
  .card svg.card__art { position: absolute; inset: 0; width: 100%; height: 100%; }

  .brand { display: flex; align-items: center; gap: 8px; white-space: nowrap; }
  .brand__dot { flex: none; width: 14px; height: 14px; border-radius: 50%; background: var(--plum); }
  .brand__name { color: var(--leaf); font-size: 34px; line-height: 1; }
  .brand__tagline {
    color: var(--plum);
    font-size: 10px;
    letter-spacing: 1.6px;
    margin-top: 4px;
    white-space: nowrap;
  }

  .front__content {
    position: absolute;
    top: 22px;
    right: 24px;
    width: 270px;
  }
  .front__person { text-align: right; margin-top: 22px; }
  .front__name { color: var(--plum); font-size: 23px; line-height: 1; }
  .front__role { color: var(--leaf); font-size: 14px; margin-top: 2px; }
  .front__services {
    list-style: none;
    text-align: right;
    color: var(--plum);
    font-size: 13px;
    line-height: 1.45;
    margin-top: 14px;
  }
  .front__contact {
    list-style: none;
    margin-top: 10px;
    color: var(--plum);
    font-size: 13px;
    line-height: 1;
  }
  .front__contact li {
    display: flex;
    justify-content: flex-end;
    align-items: center;
    gap: 7px;
    margin-top: 5px;
  }
  .icon {
    width: 15px; height: 15px;
    background: var(--leaf);
    border-radius: 2px;
    display: inline-flex;
    align-items: center;
    justify-content: center;
  }
  .icon svg { width: 11px; height: 11px; }

  .back__content {
    position: absolute;
    top: 70px;
    left: 250px;
  }
  .back__content .brand__name { font-size: 44px; }
  .back__content .brand__tagline { font-size: 11px; letter-spacing: 1.8px; margin-top: 10px; }
</style>
</head>
<body>

<section class="card card--front">
  <svg class="card__art" viewBox="0 0 540 309">
    <defs>
      <linearGradient id="portraitTone" x1="0" y1="0" x2="1" y2="1">
        <stop offset="0" stop-color="var(--forest-a)"/>
        <stop offset=".55" stop-color="var(--forest-b)"/>
        <stop offset="1" stop-color="#c9b49c"/>
      </linearGradient>
    </defs>
    <path role="img" aria-label="Portrait photo of the consultant outdoors among green foliage"
          d="M0 0 H180 C250 90 160 210 250 309 H0 Z" fill="url(#portraitTone)"/>
    <path d="M180 0 C250 90 160 210 250 309" fill="none" stroke="var(--leaf)" stroke-width="9"/>
    <path d="M192 0 C262 90 172 210 262 309" fill="none" stroke="var(--leaf-dark)" stroke-width="2" opacity=".6"/>
  </svg>

  <div class="front__content">
    <div class="brand">
      <span class="brand__dot"></span>
      <span class="brand__name">Willow Dawn</span>
    </div>
    <p class="brand__tagline">Turning Tension into Understanding</p>

    <div class="front__person">
      <p class="front__name">Mira Dalton</p>
      <p class="front__role">Consultant</p>
    </div>

    <ul class="front__services">
      <li>Interpersonal Mediation</li>
      <li>Collaborative Communication</li>
    </ul>

    <ul class="front__contact">
      <li>1-604-555-0182
        <span class="icon"><svg viewBox="0 0 12 12"><path d="M3 1 L5 3.5 L4 4.8 C4.7 6.3 5.7 7.3 7.2 8 L8.5 7 L11 9 L9.8 11 C5.5 10.6 1.4 6.5 1 2.2 Z" fill="#fff"/></svg></span>
      </li>
      <li>mira@willowdawn.ca
        <span class="icon"><svg viewBox="0 0 12 12"><rect x="1" y="2.5" width="10" height="7" fill="none" stroke="#fff" stroke-width="1.2"/><path d="M1 2.5 L6 6.5 L11 2.5" fill="none" stroke="#fff" stroke-width="1.2"/></svg></span>
      </li>
      <li>www.willowdawn.ca
        <span class="icon"><svg viewBox="0 0 12 12"><circle cx="6" cy="6" r="4.8" fill="none" stroke="#fff" stroke-width="1.1"/><ellipse cx="6" cy="6" rx="2" ry="4.8" fill="none" stroke="#fff" stroke-width="1"/><path d="M1.2 6 H10.8" stroke="#fff" stroke-width="1"/></svg></span>
      </li>
    </ul>
  </div>
</section>

<section class="card card--back">
  <svg class="card__art" viewBox="0 0 540 309">
    <defs>
      <linearGradient id="shoreTone" x1="0" y1="1" x2="1" y2="0">
        <stop offset="0" stop-color="var(--shore-a)"/>
        <stop offset=".5" stop-color="#4e5a58"/>
        <stop offset="1" stop-color="var(--shore-b)"/>
      </linearGradient>
      <linearGradient id="shoreFade" x1="0" y1="0" x2="1" y2="0">
        <stop offset="0" stop-color="#fff" stop-opacity="0"/>
        <stop offset="1" stop-color="#fff" stop-opacity="1"/>
      </linearGradient>
    </defs>
    <rect role="img" aria-label="Photo of stacked stones on a pebble beach beside calm water and a forested shore"
          x="0" y="0" width="240" height="309" fill="url(#shoreTone)"/>
    <rect x="160" y="0" width="80" height="309" fill="url(#shoreFade)"/>
  </svg>

  <div class="back__content">
    <div class="brand">
      <span class="brand__dot"></span>
      <span class="brand__name">Willow Dawn</span>
    </div>
    <p class="brand__tagline">Turning Tension into Understanding</p>
  </div>
</section>

</body>
</html>
```